Minimalist Modern Business Card Design, open to ideas, or cleaner version of provided files, but what logo & logo colors (with some black) as shown in files, and info for back shown in files as well.

```html
<!DOCTYPE html>
<html lang="en">
<head>
<meta charset="utf-8">
<title>Northline Fleet Care – Business Card</title>
<link rel="stylesheet" href="https://fonts.googleapis.com/css2?family=Montserrat:wght@400;500;600;700;800&display=swap">
<style>
  :root {
    --navy: #2b2a78;
    --black: #050505;
    --white: #ffffff;
    --ink: #1c1c24;
    --stage: #2b2d31;
  }
  * { margin: 0; padding: 0; box-sizing: border-box; }
  html, body { width: 1200px; height: 900px; overflow: hidden; }
  body {
    background: var(--stage);
    font-family: "Montserrat", sans-serif;
    display: flex;
    align-items: center;
    justify-content: center;
    gap: 40px;
  }
  .card {
    position: relative;
    width: 560px;
    height: 320px;
    background: var(--white);
    overflow: hidden;
    box-shadow: 0 6px 18px rgba(0,0,0,.35);
  }

  /* brand lockup */
  .brand {
    position: absolute;
    display: flex;
    align-items: center;
    gap: 12px;
    color: var(--navy);
    font-weight: 800;
    line-height: 1.02;
  }
  .brand-square {
    width: 34px; height: 34px;
    background: var(--navy);
    flex: none;
  }

  /* front */
  .front .brand { top: 46px; right: 40px; font-size: 36px; }
  .front .brand-square { width: 44px; height: 44px; }
  .person { position: absolute; left: 38px; top: 180px; }
  .person-name {
    color: var(--navy);
    font-weight: 800;
    font-size: 20px;
    letter-spacing: .5px;
  }
  .person-title {
    color: var(--ink);
    font-size: 12px;
    font-weight: 500;
    letter-spacing: 1px;
    margin-top: 4px;
  }
  .divider {
    position: absolute;
    left: 262px; top: 168px;
    width: 1px; height: 68px;
    background: var(--navy);
  }
  .contacts {
    position: absolute;
    left: 280px; top: 164px;
    list-style: none;
    font-size: 14px;
    color: var(--ink);
    font-weight: 500;
  }
  .contacts li { display: flex; align-items: center; gap: 10px; height: 25px; }
  .contacts svg { width: 14px; height: 14px; fill: var(--navy); flex: none; }
  .address-band {
    position: absolute;
    left: 0; right: 0; top: 254px;
    height: 38px;
    background: var(--navy);
    color: var(--white);
    font-size: 14px;
    font-weight: 500;
    display: flex;
    align-items: center;
    padding-left: 38px;
  }

  /* back */
  .back .brand { top: 24px; right: 44px; font-size: 26px; }
  .services-band {
    position: absolute;
    left: 0; right: 0; top: 92px; height: 118px;
    background: var(--navy);
    color: var(--white);
  }
  .specialty-band {
    position: absolute;
    left: 0; right: 0; top: 210px; bottom: 0;
    background: var(--black);
    color: var(--white);
  }
  .list { position: absolute; list-style: none; font-size: 11px; line-height: 16px; }
  .list li::before { content: "• "; }
  .list-heading {
    position: absolute;
    font-size: 11.5px;
    font-weight: 700;
    letter-spacing: .4px;
  }
  .services-left { left: 30px; top: 12px; }
  .services-heading { left: 300px; top: 12px; }
  .services-right { left: 300px; top: 30px; }
  .spec-col-1 { left: 30px; top: 16px; }
  .spec-heading { left: 210px; top: 16px; }
  .spec-col-2 { left: 210px; top: 34px; }
  .spec-col-3 { left: 390px; top: 34px; }
</style>
</head>
<body>

  <section class="card front" aria-label="Business card front">
    <div class="brand">
      <span class="brand-square"></span>
      <span class="brand-name">Northline<br>Fleet Care</span>
    </div>

    <div class="person">
      <p class="person-name">DANIEL HARPER</p>
      <p class="person-title">MANAGING DIRECTOR</p>
    </div>

    <span class="divider"></span>

    <ul class="contacts">
      <li>
        <svg viewBox="0 0 24 24" aria-hidden="true"><path d="M6.6 10.8a15.1 15.1 0 0 0 6.6 6.6l2.2-2.2a1 1 0 0 1 1-.25 11.4 11.4 0 0 0 3.6.57 1 1 0 0 1 1 1V20a1 1 0 0 1-1 1A17 17 0 0 1 3 4a1 1 0 0 1 1-1h3.5a1 1 0 0 1 1 1c0 1.250.2 2.45.57 3.57a1 1 0 0 1-.25 1z"/></svg>
        055-210 387 416
      </li>
      <li>
        <svg viewBox="0 0 24 24" aria-hidden="true"><path d="M2 5h20v14H2zm2 2v.5l8 5 8-5V7zm0 2.8V17h16V9.8l-8 5z"/></svg>
        hello@northlinefleet.com
      </li>
      <li>
        <svg viewBox="0 0 24 24" aria-hidden="true"><path d="M12 2a10 10 0 1 0 0 20 10 10 0 0 0 0-20zm6.9 6h-3a15 15 0 0 0-1.3-4A8 8 0 0 1 18.9 8zM12 4c.8 1.1 1.5 2.5 1.9 4h-3.8c.4-1.5 1.1-2.9 1.9-4zM4.3 14a8 8 0 0 1 0-4h3.4a16 16 0 0 0 0 4zm.8 2h3a15 15 0 0 0 1.3 4A8 8 0 0 1 5.1 16zm3-8h-3a8 8 0 0 1 4.3-4 15 15 0 0 0-1.3 4zM12 20c-.8-1.1-1.5-2.5-1.9-4h3.8c-.4 1.5-1.1 2.9-1.900 4zm2.3-6H9.7a14 14 0 0 1 0-4h4.6a14 14 0 0 1 0 4zm.3 6a15 15 0 0 0 1.3-4h3a8 8 0 0 1-4.3 4zm1.7-6a16 16 0 0 0 0-4h3.4a8 8 0 0 1 0 4z"/></svg>
        www.northlinefleet.com
      </li>
    </ul>

    <div class="address-band">88 Depot Road, Millbrook 30418, Eastland</div>
  </section>

  <section class="card back" aria-label="Business card back">
    <div class="brand">
      <span class="brand-square"></span>
      <span class="brand-name">Northline<br>Fleet Care</span>
    </div>

    <div class="services-band">
      <ul class="list services-left">
        <li>Shop &amp; Mobile</li>
        <li>DOT &amp; BIT Inspections</li>
        <li>All Maintenance &amp; Repairs</li>
        <li>Check Engine Lights</li>
        <li>Diags, Regens &amp; Programming</li>
        <li>Full Dealer Software</li>
      </ul>
      <p class="list-heading services-heading">SERVICES INCLUDE</p>
      <ul class="list services-right">
        <li>Capabilities</li>
        <li>PM &amp; Compliance Tracking</li>
        <li>App-Based Billing &amp; Live Updates</li>
        <li>Dealer Certified Techs</li>
        <li>Night Servicing to Avoid Downtime</li>
      </ul>
    </div>

    <div class="specialty-band">
      <ul class="list spec-col-1">
        <li>Heavy &amp; Medium Duty</li>
        <li>Corvane</li>
        <li>Ostrel</li>
        <li>Tarrowyn</li>
      </ul>
      <p class="list-heading spec-heading">SPECIALIZING IN</p>
      <ul class="list spec-col-2">
        <li>Vardo</li>
        <li>Stelvik</li>
        <li>Brannocline</li>
      </ul>
      <ul class="list spec-col-3">
        <li>Quenlow</li>
        <li>After Treatment</li>
        <li>And More</li>
      </ul>
    </div>
  </section>

</body>
</html>
```